tourism marketplace web app redesign*

Hi, I need our front-page redesigned. For the competition please submit a jpg of ABOVE THE FOLD ONLY. The full page redesign will be a revision request. URL is https://qp.trolvexa.hu/hu/index.html login:'fullhd' and password:'asdasd' (Fold is supposed to be at "Kiemelt Ajanlatok", use all elements above that. Please use at least one extra color other than the two in the logo, or you may completely change them. FOCUS should be on the central combined search box (3 dropdown, 2 calendar picker + Kereses Button) just like nestorly.com, ravimoto.com, Pelusi.com, etc... The search box is always large, central, white, we want that too. We want it to look more modern, more clean AND we want to feature a changing beautiful nature photo background (like nestorly.com).Please use our newly designed logo (in attached pdf) and use that new spelling: "ferntrail.online"

```html
<!DOCTYPE html>
<html lang="en">
<head>
<meta charset="utf-8">
<title>ferntrail.online – Book directly at the hunting ground</title>
<link href="https://fonts.googleapis.com/css2?family=Questrial&display=swap" rel="stylesheet">
<style>
  :root {
    --teal: #6db39b;
    --orange: #ff6a13;
    --text: #4f4f4f;
    --text-dark: #2e2e2e;
    --white: #ffffff;
    --border: #d6d6d6;
    --grey-block: #7d7d7d;
    --nav-bg: rgba(255, 255, 255, 0.9);
  }
  * { box-sizing: border-box; margin: 0; padding: 0; }
  html, body { width: 1200px; height: 857px; overflow: hidden; }
  body { font-family: "Questrial", "Century Gothic", sans-serif; color: var(--text); position: relative; }

  .hero-photo {
    position: absolute; inset: 0;
    background:
      linear-gradient(180deg, #5e6163 0%, #8d9092 18%, #a6a9a8 32%, #7b8a64 52%, #6c8a45 68%, #7c8f55 82%, #8d9288 100%),
      #7a8a60;
  }
  .hero-photo::after {
    content: ""; position: absolute; inset: 0;
    background: linear-gradient(90deg, rgba(40,60,35,0.55) 0%, rgba(60,80,45,0.2) 45%, rgba(0,0,0,0) 70%);
  }

  .top-bar { position: absolute; top: 0; left: 0; width: 1200px; height: 60px; }
  .pill-select {
    position: absolute; top: 12px; height: 35px;
    border: 2px solid var(--white); border-radius: 18px;
    color: var(--white); font-size: 16px;
    display: flex; align-items: center; padding-left: 15px;
  }
  .pill-select svg { position: absolute; right: 12px; top: 13px; }
  .lang { left: 668px; width: 130px; }
  .currency { left: 807px; width: 89px; }
  .account { position: absolute; left: 908px; top: 19px; color: var(--white); font-size: 16.5px; display: flex; align-items: center; gap: 9px; }

  .main-nav { position: absolute; top: 60px; left: 0; width: 1200px; height: 75px; background: var(--nav-bg); }
  .brand { position: absolute; left: 111px; top: 12px; display: flex; align-items: center; gap: 11px; }
  .brand-dot { width: 52px; height: 52px; border-radius: 50%; background: var(--teal); }
  .brand-name { font-size: 22px; color: var(--text-dark); }
  .nav-links { position: absolute; left: 388px; top: 29px; display: flex; gap: 13px; font-size: 15.5px; color: var(--text-dark); list-style: none; }
  .partner-btn {
    position: absolute; left: 918px; top: 18px; width: 170px; height: 39px;
    background: var(--teal); color: var(--white); border-radius: 13px;
    font-size: 15.5px; display: flex; align-items: center; justify-content: center;
  }

  .search-card {
    position: absolute; left: 112px; top: 209px; width: 471px; height: 545px;
    background: var(--white); border-radius: 17px; border-top: 9px solid var(--teal);
    overflow: hidden;
  }
  .search-card > * { position: absolute; }
  .headline { left: 13px; top: 32px; font-size: 32.5px; line-height: 36px; color: var(--text); font-weight: 700; width: 440px; }
  .tagline { left: 12px; top: 128px; font-size: 21px; color: var(--text); }
  .type-btn {
    top: 178px; height: 42px; border-radius: 14px; color: var(--white);
    font-size: 15px; display: flex; align-items: center; justify-content: center;
  }
  .type-individual { left: 11px; width: 132px; background: var(--teal); }
  .type-group { left: 148px; width: 157px; background: var(--orange); }
  .type-exclusive { left: 311px; width: 149px; background: var(--teal); }

  .field {
    height: 42px; border: 2px solid var(--border); border-radius: 14px;
    font-size: 15px; color: var(--text-dark); display: flex; align-items: center; padding-left: 12px;
  }
  .field svg { position: absolute; right: 13px; top: 16px; }
  .field-wild { left: 14px; top: 251px; width: 443px; }
  .field-country { left: 14px; top: 303px; width: 218px; }
  .field-offer { left: 240px; top: 303px; width: 217px; }
  .field-dates { left: 14px; top: 354px; width: 443px; padding: 0; overflow: hidden; }
  .date-toggle { position: absolute; left: 190px; top: 0; width: 60px; height: 100%; background: var(--grey-block); display: flex; align-items: center; justify-content: center; }

  .search-btn {
    left: 14px; top: 411px; width: 117px; height: 40px; border-radius: 14px;
    background: var(--orange); color: var(--white); font-size: 19px;
    display: flex; align-items: center; justify-content: center;
  }
  .quick-links { left: 14px; top: 484px; display: flex; gap: 15px; font-size: 16px; color: var(--text-dark); }
  .quick-links span { display: flex; align-items: center; gap: 6px; }
</style>
</head>
<body>
  <div class="hero-photo" role="img" aria-label="Nature photo: misty mountain valley with pine forest, green meadows and a winding river under cloudy sky"></div>

  <header class="top-bar">
    <div class="pill-select lang">Hungarian
      <svg width="11" height="7" viewBox="0 0 11 7"><path d="M0 0h11L5.5 7z" fill="#fff"/></svg>
    </div>
    <div class="pill-select currency">EUR
      <svg width="11" height="7" viewBox="0 0 11 7"><path d="M0 0h11L5.5 7z" fill="#fff"/></svg>
    </div>
    <div class="account">
      <svg width="17" height="17" viewBox="0 0 17 17" fill="none" stroke="#fff" stroke-width="1.6"><circle cx="8.5" cy="5" r="3.8"/><path d="M1.5 16c0-4 3-6 7-6s7 2 7 6z"/></svg>
      Registration / Login
    </div>
  </header>

  <nav class="main-nav">
    <div class="brand"><span class="brand-dot"></span><span class="brand-name">ferntrail.online</span></div>
    <ul class="nav-links">
      <li>Countries</li><li>Wild Species</li><li>About</li><li>Terms and Conditions</li><li>How It Works</li>
    </ul>
    <div class="partner-btn">Become Our Partner</div>
  </nav>

  <section class="search-card">
    <h1 class="headline">You don't need a hunting organizer!</h1>
    <p class="tagline">Book directly at the hunting ground</p>
    <div class="type-btn type-individual">Individual Hunts</div>
    <div class="type-btn type-group">Group Hunts, Shoots</div>
    <div class="type-btn type-exclusive">Exclusive Packages</div>

    <div class="field field-wild">All Wild
      <svg width="11" height="7" viewBox="0 0 11 7"><path d="M0 0h11L5.5 7z" fill="#222"/></svg>
    </div>
    <div class="field field-country">All Countries
      <svg width="11" height="7" viewBox="0 0 11 7"><path d="M0 0h11L5.5 7z" fill="#222"/></svg>
    </div>
    <div class="field field-offer">All Offers
      <svg width="11" height="7" viewBox="0 0 11 7"><path d="M0 0h11L5.5 7z" fill="#222"/></svg>
    </div>
    <div class="field field-dates">
      <div class="date-toggle">
        <svg width="22" height="16" viewBox="0 0 22 16"><path d="M10 0L1 8l9 8z M12 0l9 8-9 8z" fill="#fff"/></svg>
      </div>
    </div>

    <div class="search-btn">Search</div>

    <div class="quick-links">
      <span><svg width="12" height="17" viewBox="0 0 12 17"><path d="M6 0a6 6 0 0 0-6 6c0 4.5 6 11 6 11s6-6.5 6-11a6 6 0 0 0-6-6z" fill="#ff6a13"/><circle cx="6" cy="6" r="2.2" fill="#fff"/></svg>123456 area</span>
      <span><svg width="17" height="17" viewBox="0 0 17 17"><path d="M0 0h8l9 9-8 8-9-9z" fill="#ff6a13"/><circle cx="4" cy="4" r="1.5" fill="#fff"/></svg>Offer 87654321</span>
      <span><svg width="17" height="17" viewBox="0 0 17 17" fill="none" stroke="#ff6a13" stroke-width="2.6"><circle cx="7" cy="7" r="5"/><path d="M11 11l5 5"/></svg>Advanced Search</span>
    </div>
  </section>
</body>
</html>
```